Bellwyn Strategic

Business Development Consulting Firm

Target Market(s)

Federal Government, 8(a) companies, Small Businesses

Industry/Entity Type

Private Sector, US Government

Contact Information for Business Card

8(a) Program Capture, Business Development, Industry Trends & Analysis, Strategic Teaming, Cyber Solutions

Colors

Designer to choose colors to be used in the design.

```html
<!DOCTYPE html>
<html lang="en">
<head>
<meta charset="utf-8">
<title>Bellwyn Strategic – Business Card</title>
<link rel="stylesheet" href="https://fonts.googleapis.com/css2?family=Open+Sans:wght@400;600;700&display=swap">
<style>
  :root {
    --page-bg: #222222;
    --card-bg: #161616;
    --gold: #e2b85a;
    --gold-light: #f1d27a;
    --text-light: #f2f2f2;
  }
  * { box-sizing: border-box; margin: 0; padding: 0; }
  html, body { width: 1200px; height: 780px; overflow: hidden; }
  body {
    background: var(--page-bg);
    font-family: "Open Sans", Arial, sans-serif;
    display: flex;
    align-items: center;
    justify-content: center;
    gap: 28px;
  }
  .card {
    width: 560px;
    height: 320px;
    background: var(--card-bg);
    border-left: 5px solid var(--gold);
    border-bottom: 5px solid var(--gold);
    position: relative;
    display: flex;
    align-items: center;
    box-shadow: 0 18px 40px rgba(0,0,0,0.45);
  }
  .brand {
    display: flex;
    align-items: center;
    gap: 14px;
    color: var(--gold);
    font-weight: 700;
    text-transform: uppercase;
    line-height: 1;
  }
  .brand-mark { flex: none; }
  .brand-name { letter-spacing: 0.06em; }

  .card-front { justify-content: center; }
  .card-front .brand-name { font-size: 34px; }

  .card-back { padding: 0 34px 0 40px; }
  .card-back .brand { width: 250px; }
  .card-back .brand-name { font-size: 19px; }
  .divider {
    width: 1px;
    height: 150px;
    background: var(--gold);
    margin: 0 26px 0 10px;
  }
  .contact { color: var(--text-light); font-size: 12.5px; line-height: 1.45; }
  .person-name {
    color: var(--gold);
    font-weight: 700;
    font-size: 18px;
    text-transform: uppercase;
    letter-spacing: 0.02em;
  }
  .person-role { margin-bottom: 14px; font-size: 13px; }
  .contact-list { list-style: none; margin-bottom: 8px; }
  .contact-list li { display: flex; align-items: center; gap: 7px; }
  .contact-icon { width: 11px; height: 11px; flex: none; }
  .address { padding-left: 18px; }
</style>
</head>
<body>
  <section class="card card-front" aria-label="Card front">
    <div class="brand">
      <svg class="brand-mark" width="44" height="44" viewBox="0 0 44 44" aria-hidden="true">
        <circle cx="22" cy="22" r="18" fill="none" stroke="var(--gold)" stroke-width="4"/>
      </svg>
      <span class="brand-name">Bellwyn Strategic</span>
    </div>
  </section>

  <section class="card card-back" aria-label="Card back">
    <div class="brand">
      <svg class="brand-mark" width="28" height="28" viewBox="0 0 28 28" aria-hidden="true">
        <circle cx="14" cy="14" r="11" fill="none" stroke="var(--gold)" stroke-width="3"/>
      </svg>
      <span class="brand-name">Bellwyn Strategic</span>
    </div>
    <div class="divider"></div>
    <div class="contact">
      <p class="person-name">Marcus Hale</p>
      <p class="person-role">Managing Director</p>
      <ul class="contact-list">
        <li>
          <svg class="contact-icon" viewBox="0 0 12 12" aria-hidden="true"><path d="M2.5 1 L4.5 1 L5.3 3.5 L4 4.5 Q5 6.8 7.5 8 L8.5 6.7 L11 7.5 L11 9.5 Q10.5 11 9 11 Q1 10 1 2.8 Q1 1.2 2.5 1Z" fill="var(--gold)"/></svg>
          <span>555 204 318</span>
        </li>
        <li>
          <svg class="contact-icon" viewBox="0 0 12 12" aria-hidden="true"><rect x="0.8" y="2.5" width="10.4" height="7" fill="none" stroke="var(--gold)" stroke-width="1.2"/><path d="M1 3 L6 6.8 L11 3" fill="none" stroke="var(--gold)" stroke-width="1.2"/></svg>
          <span>info@bellwynmail.com</span>
        </li>
        <li>
          <svg class="contact-icon" viewBox="0 0 12 12" aria-hidden="true"><circle cx="6" cy="6" r="5" fill="none" stroke="var(--gold)" stroke-width="1.2"/><path d="M1 6 H11 M6 1 Q3 6 6 11 M6 1 Q9 6 6 11" fill="none" stroke="var(--gold)" stroke-width="1"/></svg>
          <span>www.bellwynstrategic.com</span>
        </li>
      </ul>
      <p class="address">48 Harlow Street, Arden<br>Virginia, Zip 2204</p>
    </div>
  </section>
</body>
</html>
```